Real Estate Investment Company Needs A Business Card Designed

I need a business card designed for my use. We are a real estate investment company based in Omaha, Nebraska that specializes in buying, rehabbing and selling single family and multifamily properties. Would love designs that incorporate our logo and colors

Industry/Entity Type

Business

Contact Information for Business Card

Marlow Pettigrew | President & CEO
4837 North 52nd Avenue, Ste 200
Omaha, NE 68214
(402) 555-7428
marlow@quillfenhomes.example
www.QuillfenHomes.example

Font styles to use
Serif

Colors
0255a3
3276b5

Requirements
Must have
• Our logo

```html
<!DOCTYPE html>
<html lang="en">
<head>
<meta charset="utf-8">
<title>Quillfen Homes – Business Card</title>
<link rel="stylesheet" href="https://fonts.googleapis.com/css2?family=Lato:wght@400;700;900&display=swap">
<style>
  :root {
    --page-bg: #e4e7eb;
    --card-bg: #f5f6f8;
    --blue-light: #4fa3ee;
    --blue-deep: #2d7cc9;
    --brand-blue: #3276b5;
    --ring-grey: #cfd1d4;
    --ring-grey-dark: #b9bcc0;
    --white: #ffffff;
  }
  * { margin: 0; padding: 0; box-sizing: border-box; }
  html, body { width: 1200px; height: 900px; overflow: hidden; }
  body {
    background: var(--page-bg);
    font-family: "Lato", Arial, sans-serif;
    position: relative;
  }
  .business-card {
    position: absolute;
    left: 120px;
    top: 154px;
    width: 960px;
    height: 592px;
    background: var(--card-bg);
    box-shadow: 0 10px 30px rgba(0,0,0,0.12);
    overflow: hidden;
  }
  .card-shapes { position: absolute; inset: 0; }
  .brand-name {
    position: absolute;
    left: 207px;
    top: 430px;
    transform: translateX(-50%);
    white-space: nowrap;
    font-weight: 900;
    font-size: 40px;
    letter-spacing: 1px;
    color: var(--brand-blue);
  }
  .contact-block {
    position: absolute;
    right: 44px;
    top: 118px;
    text-align: right;
    color: var(--white);
  }
  .person-name {
    font-weight: 700;
    font-size: 32px;
    line-height: 36px;
    letter-spacing: 0.5px;
  }
  .person-title {
    font-size: 24px;
    line-height: 30px;
  }
  .address {
    margin-top: 44px;
    font-size: 26px;
    line-height: 35px;
  }
  .contact-lines {
    margin-top: 14px;
    font-size: 26px;
    line-height: 36px;
  }
  .contact-line {
    display: flex;
    justify-content: flex-end;
    align-items: center;
    gap: 6px;
  }
  .contact-icon { width: 20px; height: 20px; flex: none; }
</style>
</head>
<body>
  <div class="business-card">
    <svg class="card-shapes" width="960" height="592" viewBox="0 0 960 592">
      <defs>
        <linearGradient id="panelBlue" x1="0" y1="0" x2="0.3" y2="1">
          <stop offset="0" stop-color="var(--blue-light)"/>
          <stop offset="1" stop-color="var(--blue-deep)"/>
        </linearGradient>
        <linearGradient id="ringGrey" x1="0" y1="0" x2="0" y2="1">
          <stop offset="0" stop-color="var(--ring-grey)"/>
          <stop offset="0.5" stop-color="var(--ring-grey-dark)"/>
          <stop offset="1" stop-color="var(--ring-grey)"/>
        </linearGradient>
      </defs>
      <circle class="accent-ring" cx="680" cy="296" r="300" fill="url(#ringGrey)"/>
      <circle class="accent-gap" cx="702" cy="296" r="298" fill="var(--card-bg)"/>
      <g class="contact-panel" fill="url(#panelBlue)">
        <circle cx="712" cy="296" r="296"/>
        <rect x="712" y="0" width="248" height="592"/>
      </g>
    </svg>

    <div class="brand-name">QUILLFEN HOMES</div>

    <div class="contact-block">
      <div class="person-name">MARLOW PETTIGREW</div>
      <div class="person-title">President &amp; CEO</div>
      <div class="address">
        4837 North 52nd Avenue, Ste 200<br>
        Omaha, NE 68214
      </div>
      <div class="contact-lines">
        <div class="contact-line">(402) 555-7428
          <svg class="contact-icon" viewBox="0 0 20 20"><path fill="#fff" d="M3 8c0-3 3-4 7-4s7 1 7 4v1h-3V7.5H6V9H3z"/><path fill="#fff" d="M5 10h10l1 6H4z"/><circle cx="10" cy="13" r="1.6" fill="#3a8ad8"/></svg>
        </div>
        <div class="contact-line">marlow@quillfenhomes.example
          <svg class="contact-icon" viewBox="0 0 20 20"><rect x="2" y="4" width="16" height="12" fill="#fff"/><path d="M2.5 4.5l7.5 6 7.5-6" fill="none" stroke="#3a8ad8" stroke-width="1.4"/></svg>
        </div>
        <div class="contact-line">www.QuillfenHomes.example
          <svg class="contact-icon" viewBox="0 0 20 20"><circle cx="10" cy="10" r="8" fill="#fff"/><path d="M6 6c2 1 3 0 4 2s-2 2-1 4 2 3 1 5M13 4c-1 2 1 3 3 3" fill="none" stroke="#3a8ad8" stroke-width="1.6"/></svg>
        </div>
      </div>
    </div>
  </div>
</body>
</html>
```